Business Card & Stationary Design for a PI Law Firm
Trial Attorneys Representing Injured Persons
I need double sided standard sized Business Card [3.5" x 2"]
use clean, modern fonts (ex: similar to a century gothic)
Bright & Fun-filled
Gregory T. Vasko
Vasko Legal Partners, LLC
418 N. Harlowe
Suite 0714
Chicago, IL 60417
vaskolegal@mailvo.net
www.vaskolegalpartners.net
Trial Attorneys Representing Injured Persons (Insert this tag line)
BUSINESS CARDS – double sided
The options are to do an assortment (up to 3) of the following:
1. front side in chocolate brown and back side in white (OR)
2. front side in the slate grey and back side in white
3. front side in lime green and back side in white
4. front side in orange and back side in white
STATIONARY:
The options are to utilize an assortment (up to 3) of the following options:
1. white background
2. white background with contrasting design elements in lime green
3. white background with contrasting design elements in orange
4. white background with contrasting design elements in chocolate brown
5. white background with contrasting design elements in slate grey
6. OR any combination of the above colors
ENVELOPES:
The options are to utilize an assortment (up to 3) of the following color options:
1. chocolate brown background
2. slate grey background
3. white background with contrast envelope fold color in slate grey
4. White background with contrast envelope fold chocolate brown
5. white background with contrast envelope fold in the lime green
6.. white background with contrast envelope fold in the orange
7. OR any combination of the above colors
WATERMARK-LIKE GRAPHICS in Stationary, Envelopes and Cards:
We would like to see a creative use of graphics for watermarks or shadows in the background of the business cards, stationery and envelopes. They can be colorful in lime green or orange or a combo of both or in chocolate brown and / or slate grey, but not too dark in saturation (as to be able to see any fonts).
LAYOUT for Cards and Stationary:
1. The layout should be clean and modern and utilize attractive and modern graphic symbols or mod bullet type points before each line of contact information.
2. Open to vertical layout or horizontal on business card.
3. Please include web address on envelope design perhaps in a separate area of the envelope from the return address.
White version

```html
<!DOCTYPE html>
<html lang="en">
<head>
<meta charset="utf-8">
<title>Vasko Legal Partners – Business Card</title>
<link href="https://fonts.googleapis.com/css2?family=Questrial&display=swap" rel="stylesheet">
<style>
  :root {
    --stage: #e8e5e0;
    --brown: #4b2a12;
    --orange: #f26b1d;
    --lime: #8cc63f;
    --white: #ffffff;
    --ink: #5a4a3e;
  }
  html, body {
    margin: 0;
    width: 1200px;
    height: 629px;
    overflow: hidden;
    background: var(--stage);
    font-family: "Questrial", "Century Gothic", sans-serif;
  }
  .stage {
    position: relative;
    width: 1200px;
    height: 629px;
  }
  .card {
    position: absolute;
    top: 166px;
    width: 520px;
    height: 297px;
    box-shadow: 0 6px 18px rgba(0,0,0,.18);
    overflow: hidden;
  }
  .card-back {
    left: 50px;
    background: var(--brown);
  }
  .card-back .web {
    position: absolute;
    left: 28px;
    bottom: 24px;
    color: var(--orange);
    font-size: 14px;
    letter-spacing: 1px;
  }
  .card-front {
    left: 630px;
    background: var(--white);
  }
  .card-front .bands {
    position: absolute;
    inset: 0;
  }
  .brand {
    position: absolute;
    left: 0;
    right: 0;
    top: 44px;
    display: flex;
    justify-content: center;
    align-items: center;
    gap: 10px;
  }
  .brand-name {
    color: var(--orange);
    font-size: 30px;
    letter-spacing: .5px;
  }
  .brand-dot {
    width: 16px;
    height: 16px;
    border-radius: 50%;
    background: var(--lime);
  }
  .person {
    position: absolute;
    left: 210px;
    top: 112px;
    color: var(--ink);
    font-size: 13px;
    line-height: 1.35;
  }
  .person .firm { font-size: 10px; }
  .address {
    position: absolute;
    left: 26px;
    bottom: 22px;
    color: var(--white);
    font-size: 11px;
    line-height: 1.45;
  }
  .contacts {
    position: absolute;
    left: 290px;
    top: 178px;
    margin: 0;
    padding: 0;
    list-style: none;
    color: var(--white);
    font-size: 11px;
  }
  .contacts li {
    display: flex;
    align-items: center;
    gap: 8px;
    height: 20px;
  }
  .contacts svg { flex: none; }
</style>
</head>
<body>
<main class="stage">

  <section class="card card-back" aria-label="Business card back">
    <span class="web">www.vaskolegalpartners.net</span>
  </section>

  <section class="card card-front" aria-label="Business card front">
    <svg class="bands" width="520" height="297" viewBox="0 0 520 297" aria-hidden="true">
      <path d="M0 178 C150 150 330 170 520 130 L520 297 L0 297 Z" fill="var(--lime)"/>
      <path d="M0 186 C150 160 330 178 520 140 L520 297 L0 297 Z" fill="var(--white)"/>
      <path d="M0 192 C150 166 330 184 520 146 L520 297 L0 297 Z" fill="var(--orange)"/>
    </svg>

    <div class="brand">
      <span class="brand-name">Vasko Legal Partners</span>
      <span class="brand-dot"></span>
    </div>

    <div class="person">
      <div class="name">Gregory T. Vasko</div>
      <div class="firm">Vasko Legal Partners, LLC</div>
    </div>

    <div class="address">
      418 N. Harlowe<br>
      Suite 0714<br>
      Chicago, IL 60417
    </div>

    <ul class="contacts">
      <li>
        <svg width="14" height="14" viewBox="0 0 14 14" aria-hidden="true"><circle cx="7" cy="7" r="7" fill="var(--white)"/><path d="M4.5 3.5 L6 3.5 L6.5 5.5 L5.6 6.2 Q6.5 8 7.8 8.4 L8.5 7.5 L10.5 8 L10.5 9.5 Q7 10.5 4.5 6 Z" fill="var(--orange)"/></svg>
        312.555.0148
      </li>
      <li>
        <svg width="14" height="14" viewBox="0 0 14 14" aria-hidden="true"><circle cx="7" cy="7" r="7" fill="var(--white)"/><rect x="4" y="4" width="6" height="6" fill="var(--orange)"/><rect x="5" y="5" width="4" height="1.2" fill="var(--white)"/></svg>
        312.555.0149
      </li>
      <li>
        <svg width="14" height="14" viewBox="0 0 14 14" aria-hidden="true"><circle cx="7" cy="7" r="7" fill="var(--white)"/><rect x="3.5" y="4.5" width="7" height="5" fill="var(--orange)"/><path d="M3.5 4.5 L7 7.3 L10.5 4.5" stroke="var(--white)" stroke-width="0.8" fill="none"/></svg>
        vaskolegal@mailvo.net
      </li>
      <li>
        <svg width="14" height="14" viewBox="0 0 14 14" aria-hidden="true"><circle cx="7" cy="7" r="7" fill="var(--white)"/><circle cx="7" cy="7" r="3.5" stroke="var(--orange)" stroke-width="1" fill="none"/><path d="M3.5 7 H10.5 M7 3.5 V10.5" stroke="var(--orange)" stroke-width="0.8"/></svg>
        www.vaskolegalpartners.net
      </li>
    </ul>
  </section>

</main>
</body>
</html>
```